Wordpress template re-design of current website

We need a WordPress template design and new look for our existing website. Our existing site it located at www.velmoro.com.au We are a tech company and want a fresh, clean modern website that matches our brand, services and logo colors. Our main Services are hospitality solutions, Velmoro TV solution and managed networks, more information on these can come from our existing website.

Target Market(s)

We are a tech company so must have a modern feel for new technology

Industry/Entity Type

It Company

Number of Pages Required

5+ page

Font styles to use
Sans Serif

Requirements
Must have
• Be based on a wordpress templete design and match the services that we have in our existing website, in the testimonials want a place for video testimonials as well as text. Nice clean icons used for graphics to represent services.
Nice to have
• nice visual representation of our services in the way of clean icons etc
Should not have
• Clutter

```html
<!DOCTYPE html>
<html lang="en">
<head>
<meta charset="utf-8">
<title>Velmoro Wireless</title>
<link href="https://fonts.googleapis.com/css2?family=Open+Sans:wght@300;400;600;700&display=swap" rel="stylesheet">
<style>
:root{
  --blue:#1c5ea8;
  --navy:#173f78;
  --band:#2b64a6;
  --grey-band:#e4e4e4;
  --text:#555;
  --light:#f5f5f5;
  --red:#d7141e;
  --orange:#e67e22;
  --cyan:#4fd6e6;
  --indigo:#3d5a98;
  --gold:#e8891c;
}
*{box-sizing:border-box;margin:0;padding:0}
html,body{width:1200px;height:2748px;overflow:hidden}
body{position:relative;font-family:'Open Sans',Arial,sans-serif;color:var(--text);background:#fff}
.abs{position:absolute}

/* hero */
.hero-photo{left:0;top:0;width:1200px;height:852px;background:linear-gradient(100deg,#e9e6e1 0%,#d8d2c8 30%,#7b4e36 55%,#4a2c1e 75%,#5b3a28 100%)}
.site-header{left:0;top:0;width:1200px;height:137px;background:rgba(255,255,255,.93);border-bottom:4px solid var(--blue)}
.brand{left:79px;top:36px;display:flex;align-items:center;gap:12px}
.brand-dot{width:34px;height:34px;border-radius:50%;background:var(--blue)}
.brand-name{font-size:40px;font-weight:700;color:var(--blue);line-height:1}
.top-contact{right:53px;top:26px;display:flex;align-items:center;gap:9px;font-size:15px;font-weight:600;color:var(--navy)}
.social-dot{width:24px;height:24px;border-radius:50%;border:1.5px solid var(--navy)}
.main-nav{top:70px;left:0;width:1200px}
.main-nav a{position:absolute;font-size:16px;font-weight:600;color:var(--navy);text-decoration:none;white-space:nowrap}
.main-nav .active::after{content:"";position:absolute;left:-6px;right:-6px;top:28px;height:4px;background:#777}
.slide-arrow{top:473px;width:46px;height:42px;display:flex;align-items:center;justify-content:center}
.slide-arrow.prev{left:0;background:rgba(120,160,200,.8)}
.slide-arrow.next{right:0;background:#1b3e6c}

.quick-contact{left:95px;top:407px;width:528px;height:192px;background:rgba(55,55,55,.78);padding:16px 17px}
.quick-contact h2{font-size:32px;font-weight:400;color:#fff;line-height:1}
.field{position:absolute;background:#e8e8e8;font-size:13px;color:#555;padding:6px 9px}
.btn{position:absolute;background:var(--blue);color:#fff;font-size:15px;display:flex;align-items:center;justify-content:center}
.hero-message{left:95px;top:610px;width:528px;height:141px;background:rgba(55,55,55,.78)}
.hero-message p{position:absolute;left:43px;top:20px;font-size:31px;font-weight:400;color:#fff;line-height:1.3}

/* partners */
.partners{left:0;top:852px;width:1200px;height:119px;background:var(--grey-band)}
.partner-badge{position:absolute;top:40px;height:40px;border-radius:4px;background:#b8b8b8}

/* services */
.section-title{left:0;width:1200px;text-align:center;color:var(--blue);font-weight:400}
.service{top:1081px;width:246px;height:271px;text-align:center}
.service.featured{background:var(--light);border:1px solid #e2e2e2;border-radius:3px}
.service .icon{width:103px;height:103px;border-radius:50%;margin:38px auto 0;display:flex;align-items:center;justify-content:center;font-size:44px;color:#fff;font-weight:600}
.service h3{font-size:25px;font-weight:400;color:var(--blue);margin-top:32px;line-height:1.1}
.service p{font-size:13.5px;line-height:1.3;color:#555;margin:8px auto 0;width:220px}

.statement{left:0;top:1429px;width:1200px;height:233px;background:linear-gradient(90deg,#5a3c2c 0%,#7a5a48 30%,#8c2a22 60%,#b9a999 100%)}
.statement p{position:absolute;left:0;top:52px;width:1200px;text-align:center;font-size:35px;font-weight:300;color:#fff;line-height:1.15}

/* testimonials */
.avatar{top:1768px;width:72px;height:72px}
.carousel-arrow{top:1792px}
.quote-box{left:174px;top:1885px;width:861px;height:178px;background:var(--light);border:1px solid #d8d8d8;border-radius:3px;padding:30px 28px}
.quote-box p{font-size:13.5px;line-height:1.7;color:#444}
.quote-box .author{text-align:center;color:var(--gold);font-weight:700;margin-top:8px}
.pointer{left:562px;top:1850px}

/* work */
.latest-work{left:0;top:2110px;width:1200px;height:257px;background:var(--band)}
.work-thumb{top:2211px;width:180px;height:118px;border-radius:6px;box-shadow:0 2px 6px rgba(0,0,0,.3)}
.see-more{left:945px;top:2230px;font-size:21px;color:#fff;line-height:1.2}

/* footer */
.footer-heading{font-size:14px;font-weight:700;color:var(--navy)}
.footer-list{font-size:13.5px;color:#555;line-height:22px;list-style:none}
.contact-line{left:119px;display:flex;align-items:flex-start;gap:12px;font-size:13.5px;color:#555;line-height:18px}
.map{left:744px;top:2490px;width:333px;height:135px;background:linear-gradient(90deg,#efeadf 0%,#e8e4d6 70%,#a9cdee 78%,#a9cdee 100%);border:1px solid #ccc}
.legal-bar{left:0;top:2675px;width:1200px;height:73px;background:#f2f2f2;border-top:1px solid #e0e0e0}
.legal-bar .copy{position:absolute;left:112px;top:28px;font-size:13px;color:#555}
.legal-bar .policy{position:absolute;left:1008px;top:28px;font-size:13px;color:#555}
.legal-social{position:absolute;top:24px;width:25px;height:25px;border-radius:50%;border:1.5px solid var(--navy)}
</style>
</head>
<body>

<div class="abs hero-photo" role="img" aria-label="Hotel bedroom with bed linen, bedside table, water jug and glass"></div>

<header class="abs site-header">
  <div class="abs brand"><span class="brand-dot"></span><span class="brand-name">Velmoro</span></div>
  <div class="abs top-contact">
    <span class="social-dot"></span><span class="social-dot"></span>
    <svg width="18" height="18" viewBox="0 0 24 24"><path d="M6.6 10.8a15 15 0 0 0 6.6 6.6l2.2-2.2c.3-.3.7-.4 1-.2 1.1.4 2.3.6 3.6.6.6 0 1 .4 1 1V20c0 .6-.4 1-1 1A17 17 0 0 1 3 4c0-.6.4-1 1-1h3.5c.6 0 1 .4 1 1 0 1.3.2 2.5.6 3.6.1.3 0 .7-.2 1z" fill="#173f78"/></svg>
    <span>1300 555 014</span>
  </div>
  <nav class="abs main-nav">
    <a class="active" style="left:568px">Home</a>
    <a style="left:652px">Services</a>
    <a style="left:748px">About Us</a>
    <a style="left:854px">Our Work</a>
    <a style="left:964px">Contact Us</a>
    <a style="left:1081px">Portal</a>
  </nav>
</header>

<div class="abs slide-arrow prev"><svg width="14" height="20" viewBox="0 0 14 20"><path d="M10 3 3 10l7 7" stroke="#fff" stroke-width="2" fill="none"/></svg></div>
<div class="abs slide-arrow next"><svg width="14" height="20" viewBox="0 0 14 20"><path d="M4 3l7 7-7 7" stroke="#fff" stroke-width="2" fill="none"/></svg></div>

<form class="abs quick-contact">
  <h2>Quick Contact</h2>
  <div class="field" style="left:17px;top:70px;width:238px;height:30px">Name</div>
  <div class="field" style="left:272px;top:70px;width:239px;height:30px">Email</div>
  <div class="field" style="left:17px;top:116px;width:494px;height:59px">Comments/ Query</div>
  <div class="btn" style="left:412px;top:145px;width:99px;height:30px">Read More</div>
</form>

<div class="abs hero-message">
  <p>Lorem ipsum dolor sit amet,<br>consectetur adipiscing elit.</p>
  <div class="btn" style="left:211px;top:128px;width:97px;height:28px">Follow Us</div>
  <div class="btn" style="left:317px;top:128px;width:30px;height:28px"></div>
  <div class="btn" style="left:355px;top:128px;width:30px;height:28px"></div>
  <div class="btn" style="left:393px;top:128px;width:99px;height:28px">Read More</div>
</div>

<section class="abs partners">
  <span class="partner-badge" style="left:102px;width:104px"></span>
  <span class="partner-badge" style="left:284px;width:100px"></span>
  <span class="partner-badge" style="left:470px;width:88px"></span>
  <span class="partner-badge" style="left:634px;width:104px"></span>
  <span class="partner-badge" style="left:814px;width:112px"></span>
  <span class="partner-badge" style="left:990px;width:116px"></span>
</section>

<h2 class="abs section-title" style="top:1018px;font-size:32px">VELMORO WIRELESS</h2>

<div class="abs service featured" style="left:104px">
  <div class="icon" style="background:var(--red)"><svg width="50" height="40" viewBox="0 0 50 40"><g fill="none" stroke="#fff" stroke-width="4" stroke-linecap="round"><path d="M5 15a28 28 0 0 1 40 0"/><path d="M12 22a18 18 0 0 1 26 0"/><path d="M19 29a8 8 0 0 1 12 0"/></g><circle cx="25" cy="35" r="3" fill="#fff"/></svg></div>
  <h3>Wi-Fi Hotspots</h3>
  <p>Leading supplier of public access and internet billing systems</p>
</div>
<div class="abs service" style="left:350px">
  <div class="icon" style="background:var(--orange)"><svg width="50" height="46" viewBox="0 0 50 46"><g fill="none" stroke="#fff" stroke-width="4" stroke-linejoin="round"><path d="M17 4l8 8 8-8"/><rect x="6" y="13" width="38" height="28" rx="4"/></g></svg></div>
  <h3>Velmoro TV</h3>
  <p>Turn you standard TV into a full guest information system and point of sale.</p>
</div>
<div class="abs service" style="left:589px">
  <div class="icon" style="background:var(--cyan)">H</div>
  <h3>HSIA Solutions</h3>
  <p>Our guest access solutions have been built with the guest in mind and are easy to use</p>
</div>
<div class="abs service" style="left:827px">
  <div class="icon" style="background:var(--indigo)"></div>
  <h3>Social Wi-Fi</h3>
  <p>Get more out of your existing Wi-Fi with our social plug-ins to gain valuble insight into users</p>
</div>

<section class="abs statement" role="img" aria-label="Hotel room with lamp and bed with red throw">
  <p>We strive to out work our competition with an<br>effective approach and a powerful skill set, which is<br>why were industry leading.</p>
</section>

<h2 class="abs section-title" style="top:1706px;font-size:25px">See What Our Customers Have To Say About Us</h2>
<svg class="abs carousel-arrow" style="left:357px" width="16" height="22" viewBox="0 0 16 22"><path d="M11 3 4 11l7 8" stroke="#1c5ea8" stroke-width="2" fill="none"/></svg>
<div class="abs avatar" style="left:398px;background:#9a8f84" role="img" aria-label="Customer portrait"></div>
<div class="abs avatar" style="left:480px;background:#a09488" role="img" aria-label="Customer portrait"></div>
<div class="abs avatar" style="left:564px;background:#3f3530" role="img" aria-label="Customer portrait, selected"></div>
<div class="abs avatar" style="left:647px;background:#b39a86" role="img" aria-label="Customer portrait"></div>
<div class="abs avatar" style="left:729px;background:#d6d6d6" role="img" aria-label="Placeholder customer portrait"></div>
<svg class="abs carousel-arrow" style="left:817px" width="16" height="22" viewBox="0 0 16 22"><path d="M5 3l7 8-7 8" stroke="#1c5ea8" stroke-width="2" fill="none"/></svg>

<blockquote class="abs quote-box">
  <p>"Installing Velmoro Internet Solution has been a great investment for this business. The staff were very professional and easy to work with and gave us several options to consider that would work best for the business. The installation was easy and happened without any problems at all. The system is easy to use for both guests and staff, which can be tailored to suit the needs of the guest and business, which was a deciding factor. I would highly recommend Velmoro as you're in room internet solution"</p>
  <p class="author">Martin Hale – Seaview Suites Ballarat</p>
</blockquote>
<svg class="abs pointer" width="44" height="37" viewBox="0 0 44 37"><path d="M2 36 42 2v34" fill="#f5f5f5" stroke="#d8d8d8"/><path d="M3 36.5h38" stroke="#f5f5f5" stroke-width="2"/></svg>

<section class="abs latest-work"></section>
<h2 class="abs section-title" style="top:2140px;font-size:33px;color:#fff;font-weight:300">Our Latest Work</h2>
<div class="abs work-thumb" style="left:123px;background:linear-gradient(135deg,#4d6f8c,#8aa06a)" role="img" aria-label="Apartment building among trees"></div>
<div class="abs work-thumb" style="left:326px;background:linear-gradient(135deg,#7fa6cf,#e8ecef)" role="img" aria-label="Tour coach"></div>
<div class="abs work-thumb" style="left:531px;background:linear-gradient(135deg,#2a2a2a,#8a7a6a)" role="img" aria-label="Laptop and smartphone on a desk"></div>
<div class="abs work-thumb" style="left:735px;background:linear-gradient(135deg,#8fb6dc,#c8cdd2)" role="img" aria-label="Hospital building"></div>
<div class="abs see-more">See Our<br>Complete<br>Works</div>
<svg class="abs" style="left:1045px;top:2238px" width="40" height="60" viewBox="0 0 40 60"><path d="M6 4l26 26L6 56" stroke="rgba(255,255,255,.7)" stroke-width="2" fill="none"/></svg>

<footer>
  <div class="abs brand" style="left:119px;top:2412px"><span class="brand-dot" style="width:30px;height:30px"></span><span class="brand-name" style="font-size:36px">Velmoro</span></div>
  <div class="abs contact-line" style="top:2488px">
    <svg width="14" height="16" viewBox="0 0 14 16"><path d="M7 1a5 5 0 0 0-5 5c0 4 5 9 5 9s5-5 5-9a5 5 0 0 0-5-5z" fill="#1c5ea8"/><circle cx="7" cy="6" r="2" fill="#fff"/></svg>
    <span>42 Harbour Crest Drive<br>Coral Bay, QLD 4230</span>
  </div>
  <div class="abs contact-line" style="top:2526px">
    <svg width="14" height="14" viewBox="0 0 24 24"><path d="M6.6 10.8a15 15 0 0 0 6.6 6.6l2.2-2.2c.3-.3.7-.4 1-.2 1.1.4 2.3.6 3.6.6.6 0 1 .4 1 1V20c0 .6-.4 1-1 1A17 17 0 0 1 3 4c0-.6.4-1 1-1h3.5c.6 0 1 .4 1 1 0 1.3.2 2.5.6 3.6.1.3 0 .7-.2 1z" fill="#1c5ea8"/></svg>
    <span>1300 555 014</span>
  </div>
  <div class="abs contact-line" style="top:2550px">
    <svg width="14" height="14" viewBox="0 0 14 14"><rect x="1" y="3" width="12" height="8" rx="1" fill="#1c5ea8"/><path d="M1.5 3.5 7 8l5.5-4.5" stroke="#fff" fill="none"/></svg>
    <span>sales@velmoro.com.au</span>
  </div>

  <h4 class="abs footer-heading" style="left:445px;top:2455px">Navigation</h4>
  <span class="abs" style="left:429px;top:2486px;width:3px;height:14px;background:var(--navy)"></span>
  <ul class="abs footer-list" style="left:445px;top:2482px">
    <li>Home</li><li>Services</li><li>About</li><li>Our Work</li><li>Testimonials</li><li>Contact</li>
  </ul>
  <ul class="abs footer-list" style="left:579px;top:2482px">
    <li>Case Studies</li><li>News</li><li>Resellers</li>
  </ul>

  <h4 class="abs footer-heading" style="left:744px;top:2455px">Locate Us</h4>
  <div class="abs map" role="img" aria-label="Map of the south-east Queensland coast with office location marker"></div>

  <div class="abs legal-bar">
    <span class="copy">© 2015 Velmoro Wireless. All Rights Reserved.</span>
    <span class="legal-social" style="left:893px"></span>
    <span class="legal-social" style="left:927px"></span>
    <span class="legal-social" style="left:961px"></span>
    <span class="policy">Privacy Policy</span>
  </div>
</footer>

</body>
</html>
```